Christmas Collection Candle Label Design

Looking to update our existing Christmas Candle Collection labels. Labels should reflect the overall feel of our brand- www.kelvabrite.ca
Want to include some color elements. Holiday colors added into design but more muted/ earthy tones not vibrant colors . Metallic elements and line art botanical illustration. Fonts should be more align to brand
Scents
Winter Lantern
Frost Berry
Amber and Fig
Belle Étoile

```html
<!DOCTYPE html>
<html lang="en">
<head>
<meta charset="utf-8">
<title>Kelva Brite — Christmas Collection Labels</title>
<link href="https://fonts.googleapis.com/css2?family=Cormorant+Garamond:ital,wght@0,400;0,500;1,400;1,500&family=EB+Garamond:wght@400&display=swap" rel="stylesheet">
<style>
  :root {
    --canvas-bg: #e4e4e4;
    --label-bg: #ffffff;
    --ink: #2b2b2b;
    --string: #b9b9b9;
    --art-edge: #e2e2e2;
    --art-tone: #ececec;
    --art-tone-light: #f7f7f7;
    --band-olive: #6b6a50;
    --band-mauve: #9b5b62;
    --band-rose: #c99089;
    --band-wine: #7a2b28;
    --band-brick: #b9483d;
    --band-text: #f6efe9;
  }
  * { box-sizing: border-box; margin: 0; padding: 0; }
  html, body {
    width: 1200px; height: 1200px; overflow: hidden;
    background: var(--canvas-bg);
  }
  .collection { position: relative; width: 1200px; height: 1200px; }

  .label {
    position: absolute;
    width: 260px; height: 252px;
    background: var(--label-bg);
    box-shadow: 0 2px 8px rgba(0,0,0,0.08);
    overflow: hidden;
  }
  .label--winter-lantern { left: 112px; top: 245px; }
  .label--scents        { left: 457px; top: 245px; }
  .label--belle-etoile  { left: 802px; top: 245px; }
  .label--amber-fig     { left: 333px; top: 735px; }
  .label--frost-berry   { left: 702px; top: 735px; }

  .label__tagline {
    position: absolute; top: 20px; right: 18px;
    font-family: "EB Garamond", serif;
    font-size: 9.5px; color: var(--ink);
    letter-spacing: 0.02em;
  }

  .label__string {
    position: absolute; left: 42px; top: 0;
    height: 78px; width: 0;
    border-left: 1px dashed var(--string);
  }
  .label__ornament {
    position: absolute; left: 24px; top: 82px;
    width: 36px; height: 88px;
    border-radius: 45% 45% 50% 50%;
    border: 1px solid var(--art-edge);
    background: linear-gradient(180deg, var(--art-tone-light) 0%, var(--art-tone) 100%);
  }
  .label__botanical {
    position: absolute; right: 8px; top: 58px;
    width: 56px; height: 150px;
    border-radius: 60% 40% 50% 50%;
    border: 1px solid var(--art-edge);
    background: linear-gradient(200deg, var(--art-tone-light) 0%, var(--art-tone) 100%);
  }

  .label__title {
    position: absolute; left: 66px; right: 66px; top: 100px;
    text-align: center;
    color: var(--ink);
    line-height: 0.95;
    font-weight: 400;
  }
  .label__title-caps {
    display: block;
    font-family: "Cormorant Garamond", serif;
    font-weight: 500;
    font-size: 24px;
    letter-spacing: 0.01em;
  }
  .label__title-script {
    display: block;
    font-family: "Cormorant Garamond", serif;
    font-style: italic;
    font-size: 28px;
  }
  .label__title--single { top: 112px; }
  .label__title--inline .label__title-script { display: inline; font-size: 24px; }
  .label__title--inline .label__title-caps--inline { display: inline; margin-left: 3px; }

  .label__band {
    position: absolute; left: 0; right: 0; bottom: 14px;
    height: 20px;
    display: flex; align-items: center; justify-content: center; gap: 6px;
    font-family: "EB Garamond", serif;
    font-size: 8.5px; color: var(--band-text);
    white-space: nowrap;
  }
  .label__band-divider { opacity: 0.85; }
  .label--winter-lantern .label__band { background: var(--band-olive); }
  .label--scents .label__band { background: var(--band-mauve); }
  .label--belle-etoile .label__band { background: var(--band-rose); }
  .label--amber-fig .label__band { background: var(--band-wine); }
  .label--frost-berry .label__band { background: var(--band-brick); }
</style>
</head>
<body>
<main class="collection">

  <section class="label label--winter-lantern">
    <p class="label__tagline">made with plant based botanicals</p>
    <span class="label__string"></span>
    <div class="label__ornament" role="img" aria-label="Line art hanging pine cone ornament"></div>
    <div class="label__botanical" role="img" aria-label="Line art botanical leafy branch"></div>
    <h2 class="label__title">
      <span class="label__title-caps">WINTER</span>
      <span class="label__title-script">Lantern</span>
    </h2>
    <p class="label__band">Net W.T. 10oz/283g <span class="label__band-divider">|</span> Made in Canada <span class="label__band-divider">|</span> Kelva Brite</p>
  </section>

  <section class="label label--scents">
    <p class="label__tagline">made with plant based botanicals</p>
    <span class="label__string"></span>
    <div class="label__ornament" role="img" aria-label="Line art hanging fir cone ornament"></div>
    <div class="label__botanical" role="img" aria-label="Line art holly branch"></div>
    <h2 class="label__title label__title--single">
      <span class="label__title-caps">SCENTS</span>
    </h2>
    <p class="label__band">Net W.T. 10oz/283g <span class="label__band-divider">|</span> Made in Canada <span class="label__band-divider">|</span> Kelva Brite</p>
  </section>

  <section class="label label--belle-etoile">
    <p class="label__tagline">made with plant based botanicals</p>
    <span class="label__string"></span>
    <div class="label__ornament" role="img" aria-label="Line art hanging knitted mitten ornament"></div>
    <div class="label__botanical" role="img" aria-label="Line art leafy vine"></div>
    <h2 class="label__title">
      <span class="label__title-caps">BELLE</span>
      <span class="label__title-script">Étoile</span>
    </h2>
    <p class="label__band">Net W.T. 10oz/283g <span class="label__band-divider">|</span> Made in Canada <span class="label__band-divider">|</span> Kelva Brite</p>
  </section>

  <section class="label label--amber-fig">
    <p class="label__tagline">made with plant based botanicals</p>
    <span class="label__string"></span>
    <div class="label__ornament" role="img" aria-label="Line art hanging candy cane ornament with bow"></div>
    <div class="label__botanical" role="img" aria-label="Line art leaf branch"></div>
    <h2 class="label__title label__title--inline">
      <span class="label__title-caps">AMBER</span>
      <span class="label__title-script">And</span><span class="label__title-caps label__title-caps--inline">FIG</span>
    </h2>
    <p class="label__band">Net W.T. 10oz/283g <span class="label__band-divider">|</span> Made in Canada <span class="label__band-divider">|</span> Kelva Brite</p>
  </section>

  <section class="label label--frost-berry">
    <p class="label__tagline">made with plant based botanicals</p>
    <span class="label__string"></span>
    <div class="label__ornament" role="img" aria-label="Line art hanging twisted icicle ornament"></div>
    <div class="label__botanical" role="img" aria-label="Line art holly and berry branch"></div>
    <h2 class="label__title">
      <span class="label__title-caps">FROST</span>
      <span class="label__title-script">Berry</span>
    </h2>
    <p class="label__band">Net W.T. 10oz/283g <span class="label__band-divider">|</span> Made in Canada <span class="label__band-divider">|</span> Kelva Brite</p>
  </section>

</main>
</body>
</html>
```